Professional modern business card design

A business card for my nutrition business, wanting a professional look, with info clearly visible. Open to using logo colours too.

Would like key info on the front -
logo
my name and qualifications
email
phone number

and just an enlarged logo again / image on the back.

```html
<!DOCTYPE html>
<html lang="en">
<head>
<meta charset="utf-8">
<title>HL Nutrition – Business Card</title>
<link href="https://fonts.googleapis.com/css2?family=Cabin:wght@400;700&display=swap" rel="stylesheet">
<style>
  :root {
    --backdrop: #eef0ef;
    --card-white: #ffffff;
    --card-lime: #d6df22;
    --ink-navy: #2d3461;
    --ink-olive: #7a9f2e;
  }
  html, body {
    margin: 0;
    padding: 0;
    width: 1200px;
    height: 1035px;
    overflow: hidden;
    background: var(--backdrop);
  }
  .canvas {
    position: relative;
    width: 1200px;
    height: 1035px;
  }
  .card {
    position: absolute;
    top: 276px;
    width: 276px;
    height: 483px;
    border-radius: 17px;
    overflow: hidden;
    font-family: "Cabin", sans-serif;
    color: var(--ink-navy);
  }
  .card--back {
    left: 307px;
    background: var(--card-white);
  }
  .card--front {
    left: 617px;
    background: var(--card-lime);
  }
  .brand-name {
    position: absolute;
    left: 26px;
    top: 52px;
    margin: 0;
    font-weight: 700;
    font-size: 26px;
    line-height: 30px;
    white-space: nowrap;
  }
  .identity {
    position: absolute;
    right: 39px;
    top: 46px;
    text-align: right;
  }
  .identity__name {
    margin: 0;
    font-size: 21px;
    line-height: 24px;
    font-weight: 400;
  }
  .identity__name strong {
    font-weight: 700;
  }
  .identity__role {
    margin: 2px 0 0;
    font-size: 13.3px;
    line-height: 16.5px;
    color: var(--ink-olive);
  }
  .contact {
    position: absolute;
    right: 39px;
    bottom: 33px;
    text-align: right;
    font-size: 18px;
    line-height: 20px;
  }
  .contact p {
    margin: 0;
  }
</style>
</head>
<body>
  <div class="canvas">
    <section class="card card--back" aria-label="Card back">
      <p class="brand-name">HL Nutrition</p>
    </section>

    <section class="card card--front" aria-label="Card front">
      <div class="identity">
        <h1 class="identity__name">Harriet <strong>Lyle</strong></h1>
        <p class="identity__role">Specialist Rehabilitation<br>Dietitian</p>
      </div>
      <div class="contact">
        <p class="contact__phone">07700900123</p>
        <p class="contact__email">harriet@hlnutrition.co.uk</p>
      </div>
    </section>
  </div>
</body>
</html>
```